Medical Company in need of Modern business card design for new Wound Care clinic.

Modern business card design for our Woundcare company. Logo and description of services can be found on our website; https://www.tornvel-skinheal.com/

```html
<!DOCTYPE html>
<html lang="en">
<head>
<meta charset="utf-8">
<title>Tornvel Skinheal — Business Card</title>
<link href="https://fonts.googleapis.com/css2?family=Didact+Gothic&family=Arimo:wght@400;700&display=swap" rel="stylesheet">
<style>
  :root {
    --backdrop: #3d3d3d;
    --card-white: #ffffff;
    --ink: #111111;
    --text-grey: #4a4a4a;
    --muted-grey: #8a8a8a;
    --gold-light: #fbc96e;
    --gold-mid: #d9a24a;
    --gold-deep: #a87a2c;
    --gold-shadow: #7d5a22;
    --black-band: #050505;
  }
  * { box-sizing: border-box; margin: 0; padding: 0; }
  html, body {
    width: 1200px; height: 803px; overflow: hidden;
    background: var(--backdrop);
  }
  .canvas {
    width: 1200px; height: 803px;
    display: flex; align-items: center; justify-content: center; gap: 40px;
  }
  .card {
    position: relative;
    width: 540px; height: 309px;
    border-radius: 20px;
    overflow: hidden;
  }

  /* Front side */
  .card--front { background: var(--card-white); }
  .brand-block {
    position: absolute; left: 40px; top: 92px; width: 210px;
    display: flex; flex-direction: column; align-items: center; gap: 14px;
  }
  .brand-square {
    width: 26px; height: 26px;
    background: var(--gold-mid);
  }
  .brand-name {
    font-family: "Didact Gothic", sans-serif;
    font-size: 17px; letter-spacing: 4px;
    color: var(--ink); white-space: nowrap;
  }
  .divider {
    position: absolute; left: 272px; top: 40px;
    width: 1px; height: 168px;
    background: linear-gradient(to bottom, #d8d8d8, #bcbcbc);
  }
  .contact {
    position: absolute; left: 296px; top: 40px;
    font-family: "Arimo", sans-serif;
    color: var(--text-grey);
  }
  .contact__name {
    font-weight: 700; font-size: 22px;
    color: var(--gold-mid); line-height: 1;
  }
  .contact__title {
    font-size: 11px; color: var(--muted-grey);
    margin-top: 3px;
  }
  .contact__address {
    font-size: 12px; line-height: 1.3;
    margin-top: 14px;
  }
  .contact__line {
    display: flex; align-items: center; gap: 7px;
    font-size: 12px; margin-top: 5px;
  }
  .contact__line:first-of-type { margin-top: 12px; }
  .contact__icon { width: 11px; height: 11px; flex: none; }
  .web-band {
    position: absolute; left: 0; right: 0; bottom: 44px; height: 34px;
    background: linear-gradient(90deg, var(--gold-deep) 0%, var(--gold-light) 45%, var(--gold-mid) 75%, var(--gold-deep) 100%);
    display: flex; align-items: center; padding-left: 40px;
  }
  .web-band__url {
    font-family: "Arimo", sans-serif; font-size: 13px;
    color: var(--ink);
  }
  .web-band__end {
    position: absolute; right: 0; top: 0; bottom: 0; width: 60px;
    background: var(--black-band);
  }

  /* Back side */
  .card--back {
    background: radial-gradient(ellipse 70% 80% at 38% 38%, var(--gold-light) 0%, var(--gold-mid) 45%, var(--gold-deep) 85%, var(--gold-shadow) 110%);
    display: flex; flex-direction: column; align-items: center; justify-content: center; gap: 22px;
  }
  .card--back .brand-square {
    width: 40px; height: 40px;
    background: var(--ink);
  }
  .card--back .brand-name {
    font-size: 30px; letter-spacing: 7px;
  }
</style>
</head>
<body>
<main class="canvas">
  <section class="card card--front" aria-label="Business card front">
    <div class="brand-block">
      <span class="brand-square"></span>
      <span class="brand-name">TORNVEL SKINHEAL</span>
    </div>
    <div class="divider"></div>
    <div class="contact">
      <p class="contact__name">Marcus Hale</p>
      <p class="contact__title">President</p>
      <p class="contact__address">2218 Corvan Ave, Ste 100<br>PMB 408812 Dallas<br>TX 75219</p>
      <p class="contact__line">
        <svg class="contact__icon" viewBox="0 0 12 12" aria-hidden="true"><path d="M2.3 1h2l1 2.6-1.3.9a6.5 6.5 0 0 0 3.5 3.5l.9-1.3 2.6 1v2A1.3 1.3 0 0 1 9.7 11 8.8 8.8 0 0 1 1 2.3 1.3 1.3 0 0 1 2.3 1z" fill="#d9a24a"/></svg>
        972-555-0147
      </p>
      <p class="contact__line">
        <svg class="contact__icon" viewBox="0 0 12 12" aria-hidden="true"><rect x="0.5" y="2.5" width="11" height="7.5" fill="#d9a24a"/><path d="M0.8 2.8 6 6.8l5.2-4" fill="none" stroke="#fff" stroke-width="1"/></svg>
        info@tornvel-skinheal.com
      </p>
    </div>
    <div class="web-band">
      <span class="web-band__url">www.tornvel-skinheal.com</span>
      <span class="web-band__end"></span>
    </div>
  </section>

  <section class="card card--back" aria-label="Business card back">
    <span class="brand-square"></span>
    <span class="brand-name">TORNVEL SKINHEAL</span>
  </section>
</main>
</body>
</html>
```